Cover for Where the Lantern Drifts Beyond the Quiet Shore

Cover for a book that describes everything that happens to a person, from pre-birth life plans through growing in compassion and wisdom to death and living in the afterlife. The information is revealed in messages from people living in the life after this life. The title is Patterns Behind the Seasons of Your Journey and Beyond: Told by Voices Dwelling Past the Veil. Author is T. Milton Baxby. Book size is 6 by 9.

Target Market(s)

General

Font styles to use
Serif

```html
<!DOCTYPE html>
<html lang="en">
<head>
<meta charset="utf-8">
<title>Patterns Behind the Seasons of Your Journey and Beyond — Cover Spread</title>
<link rel="stylesheet" href="https://fonts.googleapis.com/css2?family=EB+Garamond:wght@400;500&display=swap">
<style>
  :root {
    --backdrop: #eeeeee;
    --paper: #ffffff;
    --ink: #1c1c1c;
    --ink-soft: #333333;
    --feather-teal: #2f6d78;
    --feather-green: #7d9c3e;
    --ornament: #4f7a3a;
    --shadow: rgba(0, 0, 0, 0.18);
  }
  * { margin: 0; padding: 0; box-sizing: border-box; }
  html, body { width: 899px; height: 1200px; overflow: hidden; background: var(--backdrop); }
  body { font-family: "EB Garamond", Garamond, serif; color: var(--ink); }

  .canvas { position: relative; width: 899px; height: 1200px; }

  .spread {
    position: absolute; left: 20px; top: 292px; width: 859px; height: 615px;
    background: var(--paper);
    box-shadow: 0 2px 10px var(--shadow);
  }

  .feather {
    position: absolute; border-radius: 50%;
    background: radial-gradient(ellipse at 60% 40%, var(--feather-teal) 0%, var(--feather-green) 70%, rgba(125,156,62,0) 100%);
  }
  .ornament {
    position: absolute; height: 5px; border-radius: 50%;
    background: var(--ornament);
  }

  /* Back cover */
  .back-cover { position: absolute; left: 0; top: 0; width: 403px; height: 615px; }
  .back-cover .feather { left: 158px; top: 114px; width: 59px; height: 22px; transform: rotate(-12deg); }
  .blurb {
    position: absolute; left: 33px; top: 181px; width: 355px;
    font-size: 8.6px; line-height: 10.6px; text-align: justify; color: var(--ink-soft);
  }
  .blurb p + p { margin-top: 10px; }

  /* Spine */
  .spine { position: absolute; left: 403px; top: 0; width: 55px; height: 615px; }
  .spine-title {
    position: absolute; left: 28px; top: 8px;
    writing-mode: vertical-rl; transform: translateX(-50%);
    font-size: 13.4px; white-space: nowrap;
  }
  .spine-author {
    position: absolute; left: 28px; top: 418px;
    writing-mode: vertical-rl; transform: translateX(-50%);
    font-size: 6.5px; letter-spacing: 2px; white-space: nowrap;
  }
  .spine .feather { left: 20px; top: 534px; width: 16px; height: 36px; transform: rotate(25deg); }

  /* Front cover */
  .front-cover { position: absolute; left: 458px; top: 0; width: 401px; height: 615px; text-align: center; }
  .front-author {
    position: absolute; left: 0; right: 0; top: 68px;
    font-size: 15px; letter-spacing: 4px;
  }
  .front-cover .feather { left: 90px; top: 210px; width: 215px; height: 62px; transform: rotate(-38deg); }
  .front-cover .ornament-top { left: 177px; top: 352px; width: 47px; }
  .front-title {
    position: absolute; left: 0; right: 0; top: 368px;
    font-size: 19px; line-height: 28px; font-weight: 400;
  }
  .front-cover .ornament-bottom { left: 177px; top: 494px; width: 47px; }
  .front-subtitle {
    position: absolute; left: 20px; right: 10px; top: 530px;
    font-size: 12px; line-height: 22px; letter-spacing: 2.6px;
  }
</style>
</head>
<body>
<main class="canvas">
  <section class="spread">
    <div class="back-cover">
      <div class="feather" role="img" aria-label="Small teal and green feather illustration"></div>
      <div class="blurb">
        <p>Lorem ipsum dolor sit amet, consectetur adipiscing elit. Maecenas aliquet aliquam leo nec pellentesque. Nam imperdiet dignissim est, in lacinia purus varius vitae. Aliquam nec tellus eget risus blandit aliquam vel nec mi. Morbi dignissim ex blandit justo efficitur gravida. Morbi vitae justo scelerisque, placerat velit nec, ornare urna. Mauris eget nunc pellentesque, vehicula ligula non, elementum nibh. Ut at porttitor magna, finibus porttitor lorem. Quisque vitae mi ac diam venenatis dapibus sed id sapien. Quisque varius, turpis sit amet tempor faucibus, magna lorem pulvinar felis, non fermentum neque tellus ut velit. Vivamus quis aliquet turpis, a auctor nunc. Proin cursus et orci eget commodo. Nam placerat sem in nisi dapibus porttitor. Nulla auctor varius leo, commodo porta eros dapibus elementum. Nullam cursus enim ac mi efficitur, vel egestas elit ultrices. Pellentesque elit augue, semper in quam at, tristique accumsan massa. Proin efficitur gravida turpis eu placerat.</p>
        <p>Nunc eros dui, dapibus sit amet eros sed, consectetur ullamcorper ipsum. Fusce auctor, ipsum non congue ullamcorper, tellus odio semper lectus, id elementum dui nibh quis lacus. Curabitur pharetra dolor id nisi bibendum aliquam. Aliquam vestibulum porta elit id varius. Aenean est mi, posuere vel nibh nec, varius malesuada eros. Ut fringilla nulla vitae mi venenatis, et suscipit tellus egestas. Curabitur in mi finibus, euismod urna ac, iaculis odio.</p>
      </div>
    </div>

    <div class="spine">
      <div class="spine-title">Patterns Behind the Seasons of Your Journey and Beyond</div>
      <div class="spine-author">T. MILTON BAXBY</div>
      <div class="feather" role="img" aria-label="Small feather illustration on the spine"></div>
    </div>

    <div class="front-cover">
      <div class="front-author">T. MILTON BAXBY</div>
      <div class="feather" role="img" aria-label="Large teal and green feather illustration"></div>
      <div class="ornament ornament-top" role="img" aria-label="Decorative green flourish"></div>
      <h1 class="front-title">Patterns Behind<br>the Seasons of Your<br>Journey and Beyond</h1>
      <div class="ornament ornament-bottom" role="img" aria-label="Decorative green flourish"></div>
      <p class="front-subtitle">Told by Voices Dwelling Past the<br>Veil</p>
    </div>
  </section>
</main>
</body>
</html>
```